Need Business Card ASAP

We need a business card design for a meeting coming up in a few days. The company name is Harwick Development and Construction and the logo is attached. Something clean, cool, and contemporary that we can get to a printer right away. Attached is the business card for Molvar Energy, an affiliated company, which we like. Instead of the hawk on the back, you could use the attached "D". We'll also be needing matching letterhead in the near future, so ideas for that are welcome.

```html
<!DOCTYPE html>
<html lang="en">
<head>
<meta charset="utf-8">
<title>Harwick Development and Construction – Stationery</title>
<link href="https://fonts.googleapis.com/css2?family=EB+Garamond:wght@400;500&family=PT+Sans:ital,wght@0,400;0,700;1,700&display=swap" rel="stylesheet">
<style>
  :root {
    --backdrop: #a9aaad;
    --paper: #dcdab8;
    --paper-light: #e6e4c9;
    --gold-deep: #b3a86a;
    --gold-light: #e2dfc3;
    --gold-text: #cdbf7d;
    --ink: #1f1a17;
    --ink-brown: #2c1d17;
    --band-dark: #6d6b5e;
    --band-light: #c9c7b0;
    --serif: "EB Garamond", Georgia, serif;
    --sans: "PT Sans", Arial, sans-serif;
  }
  * { box-sizing: border-box; margin: 0; padding: 0; }
  html, body { width: 920px; height: 1200px; overflow: hidden; }
  body {
    position: relative;
    background: linear-gradient(180deg, #b6b7ba 0%, var(--backdrop) 45%, #8f9094 100%);
    font-family: var(--sans);
    color: var(--ink);
  }

  /* shared pieces */
  .gold-square {
    position: absolute;
    background: linear-gradient(135deg, var(--gold-deep) 0%, #cfc89c 55%, var(--gold-light) 100%);
  }
  .name-block {
    position: absolute;
    background: var(--ink);
    color: var(--gold-text);
    font-family: var(--serif);
    font-weight: 400;
    display: flex;
    align-items: center;
    justify-content: center;
    text-align: center;
    line-height: 1.15;
  }
  .band {
    position: absolute;
    height: 6px;
    background: linear-gradient(180deg, var(--band-light) 0%, var(--band-dark) 50%, var(--band-light) 100%);
  }
  .address { font-family: var(--sans); font-size: 11px; line-height: 1.3; text-align: right; }
  .phone { font-family: var(--sans); font-weight: 700; font-style: italic; font-size: 11.5px; }
  .web {
    font-family: var(--sans);
    letter-spacing: 0.32em;
    font-size: 11px;
  }

  /* business card front */
  .card-front {
    position: absolute;
    left: 66px; top: 110px;
    width: 334px; height: 190px;
    background: var(--paper);
  }
  .card-front .gold-square { left: 8px; top: 8px; width: 110px; height: 104px; }
  .card-front .name-block { left: 0; top: 112px; width: 118px; height: 62px; font-size: 14px; padding: 6px; }
  .card-front .band { left: 118px; top: 36px; width: 140px; height: 5px; }
  .card-front .address { position: absolute; right: 10px; top: 8px; }
  .card-front .phones { position: absolute; right: 10px; top: 146px; text-align: right; line-height: 1.35; }

  /* business card back */
  .card-back {
    position: absolute;
    left: 445px; top: 95px;
    width: 340px; height: 194px;
    background: radial-gradient(ellipse at 60% 55%, #3a2219 0%, var(--ink-brown) 55%, #1a1411 100%);
    color: var(--gold-text);
  }
  .card-back .title {
    position: absolute; left: 0; right: 0; top: 12px;
    text-align: center; font-family: var(--serif); font-size: 15.5px;
  }
  .card-back .gold-square { left: 92px; top: 40px; width: 156px; height: 116px; }
  .card-back .web { position: absolute; left: 0; right: 0; bottom: 12px; text-align: center; font-size: 10px; }

  /* letterhead */
  .letterhead {
    position: absolute;
    left: 154px; top: 392px;
    width: 612px; height: 792px;
    background: linear-gradient(180deg, var(--paper-light) 0%, var(--paper) 100%);
  }
  .letterhead .gold-square { left: 16px; top: 16px; width: 140px; height: 124px; }
  .letterhead .name-block { left: 16px; top: 140px; width: 140px; height: 76px; font-size: 17px; padding: 8px; }
  .letterhead .title {
    position: absolute; left: 172px; top: 48px;
    font-family: var(--serif); font-size: 26px; font-weight: 400;
  }
  .letterhead .address { position: absolute; right: 40px; top: 84px; font-size: 12px; }
  .letterhead .band.top { left: 156px; top: 120px; width: 430px; }
  .letterhead .phone.main { position: absolute; left: 172px; top: 146px; font-size: 12px; }
  .letterhead .phone.fax { position: absolute; right: 40px; top: 126px; font-size: 12px; }
  .letterhead .faint-panel {
    position: absolute; left: 140px; top: 286px;
    width: 330px; height: 260px;
    background: linear-gradient(135deg, rgba(255,255,255,0.12) 0%, rgba(255,255,255,0.32) 100%);
    display: flex; align-items: center; justify-content: center;
    font-family: var(--serif); font-size: 52px; color: rgba(120,114,90,0.22);
  }
  .letterhead .band.bottom { left: 16px; top: 698px; width: 580px; }
  .letterhead .web { position: absolute; left: 0; right: 0; top: 740px; text-align: center; font-size: 13px; }
</style>
</head>
<body>

  <section class="card-front" aria-label="Business card, front">
    <div class="gold-square"></div>
    <div class="name-block">Harwick Development and Construction</div>
    <div class="band"></div>
    <p class="address">2716 W. 41st Street<br>Austin, TX 78731</p>
    <p class="phones phone">Phone: (512) 555-0148<br>Fax: (512) 555-0176</p>
  </section>

  <section class="card-back" aria-label="Business card, back">
    <p class="title">Harwick Development and Construction</p>
    <div class="gold-square"></div>
    <p class="web">www.harwickdevelopment.com</p>
  </section>

  <section class="letterhead" aria-label="Letterhead">
    <div class="gold-square"></div>
    <div class="name-block">Harwick Development and Construction</div>
    <h1 class="title">Harwick Development and Construction</h1>
    <p class="address">2716 W. 41st Street<br>Austin, TX 78731</p>
    <div class="band top"></div>
    <p class="phone fax">Fax: (512) 555-0176</p>
    <p class="phone main">Phone: (512) 555-0148</p>
    <div class="faint-panel">Harwick</div>
    <div class="band bottom"></div>
    <p class="web">www.harwickdevelopment.com</p>
  </section>

</body>
</html>
```